Bref créative
office materials
pain medicine
Professional
Marlene Dubovski, MD
Anesthesiology and Pain Medicine
4218 Lark Ave, Suite 307
Linden Bay, Florida 33190
novahealclinic@mailvora.com

```html
<!DOCTYPE html>
<html lang="en">
<head>
<meta charset="utf-8">
<title>Acheflow Pain Care – Business Cards</title>
<link href="https://fonts.googleapis.com/css2?family=Questrial&family=Mulish:wght@400;700&display=swap" rel="stylesheet">
<style>
  :root {
    --navy: #2e5b8c;
    --green: #3f8a4a;
    --white: #ffffff;
    --paper: #ffffff;
    --line: #d6d6d6;
    --text-light: #ffffff;
  }
  * { margin: 0; padding: 0; box-sizing: border-box; }
  html, body { width: 1200px; height: 703px; overflow: hidden; background: var(--paper); }
  .sheet { position: relative; width: 1200px; height: 703px; }
  .card {
    position: absolute; width: 564px; height: 314px; overflow: hidden;
    box-shadow: 0 0 0 1px var(--line);
  }
  .card--front-top { left: 17px; top: 17px; background: var(--white); }
  .card--navy { left: 619px; top: 17px; background: var(--navy); }
  .card--green { left: 17px; top: 360px; background: var(--green); }
  .card--plain { left: 619px; top: 360px; background: var(--white); }

  .card__shape { position: absolute; inset: 0; }

  .brand {
    position: absolute; display: flex; flex-direction: column; align-items: center;
    font-family: "Questrial", sans-serif; color: var(--navy); white-space: nowrap;
  }
  .brand__dot { width: 32px; height: 32px; border-radius: 50%; background: var(--green); margin-bottom: 10px; }
  .brand__name { font-size: 27px; letter-spacing: 1.5px; line-height: 1; text-transform: uppercase; }
  .brand--light { color: var(--text-light); }
  .brand--light .brand__dot { background: var(--white); }
  .brand--small .brand__dot { width: 26px; height: 26px; margin-bottom: 8px; }
  .brand--small .brand__name { font-size: 19px; letter-spacing: 1px; }

  .brand--front { left: 20px; top: 180px; width: 250px; }
  .brand--center { left: 0; right: 0; top: 112px; }

  .contact {
    position: absolute; color: var(--text-light); font-family: "Mulish", sans-serif;
  }
  .contact__person { left: 330px; top: 32px; }
  .contact__name { font-weight: 700; font-size: 14px; }
  .contact__title { font-size: 12px; margin-top: 5px; }
  .contact__details { left: 330px; top: 208px; font-size: 12px; line-height: 16.5px; }
  .contact__label { font-weight: 700; display: inline-block; width: 14px; }
</style>
</head>
<body>
<main class="sheet">

  <section class="card card--front-top" aria-label="Business card front">
    <svg class="card__shape" viewBox="0 0 564 314" aria-hidden="true">
      <path d="M 40 0 C 210 30, 300 150, 296 314 H 564 V 0 Z" fill="#3f8a4a"/>
      <path d="M 62 0 C 226 32, 312 150, 308 314 H 564 V 0 Z" fill="#2e5b8c"/>
    </svg>
    <div class="brand brand--small brand--front">
      <span class="brand__dot"></span>
      <span class="brand__name">Acheflow Pain Care</span>
    </div>
    <div class="contact contact__person">
      <p class="contact__name">Marlene Dubovski, MD</p>
      <p class="contact__title">Anesthesiology and Pain Medicine</p>
    </div>
    <div class="contact contact__details">
      <p>4218 Lark Ave, Suite 307</p>
      <p>Linden Bay, Florida 33190</p>
      <p><span class="contact__label">P</span>: 305-555-0182</p>
      <p><span class="contact__label">F</span>: 305-555-0190</p>
      <p><span class="contact__label">E</span>: novahealclinic@mailvora.com</p>
    </div>
  </section>

  <section class="card card--navy" aria-label="Business card back, navy">
    <div class="brand brand--light brand--center">
      <span class="brand__dot"></span>
      <span class="brand__name">Acheflow Pain Care</span>
    </div>
  </section>

  <section class="card card--green" aria-label="Business card back, green">
    <div class="brand brand--light brand--center">
      <span class="brand__dot"></span>
      <span class="brand__name">Acheflow Pain Care</span>
    </div>
  </section>

  <section class="card card--plain" aria-label="Business card back, white">
    <div class="brand brand--center">
      <span class="brand__dot"></span>
      <span class="brand__name">Acheflow Pain Care</span>
    </div>
  </section>

</main>
</body>
</html>
```